KFZ-Gutachter Banner

Ziel des Banners:
Der Banner soll auf die Tätigkeit als Kfz-Sachverständiger aufmerksam machen. Er wird im Außenbereich eingesetzt und soll schon aus der Ferne verständlich und gut lesbar sein.

Gestaltung:
• Schlichtes, professionelles Design (keine überladene Gestaltung, ruhige Farbwahl – anlehnend an den Farben schwarz und Rot.
• Ein Bild wo sich zwei hochwertige Autos verunfallt befinden
• Großzügige Schriftgrößen – der Text muss auch aus 20–30 m Entfernung gut lesbar sein
• Klare Informationsstruktur

Inhalte (Text):
1. Überschrift / Hauptaussage (groß & auffällig):
Kfz-Sachverständiger
oder
Unfallgutachten vom Profi
2. Kurze Beschreibung (kleiner, aber lesbar):
• Unfallgutachten
• Fahrzeugbewertung
• Technische Beratung
3. Kontaktdaten (am wichtigsten – sehr gut sichtbar & lesbar):
• Telefonnummer (z. B. groß & fett)
• Website oder E-Mail
• Optional: Standort oder “auch mobil im Einsatz”

Bildelemente:
• Optional ein dezentes Symbol oder Icon (z. B. Auto, Lupe, Checkzeichen) – nur wenn es nicht vom Text ablenkt

Format:
• Querformat, je nach Platz vor Ort (z. B. 3 m x 1,5 m)

Ingenieurbüro Lorenz Vahle Ostlinger Str.14 58706 Menden www.pruefwerk-tz.de

• Man muss sofort erkennen, dass es sich um einen KFZ-Gutachter handelt.

```html
<!DOCTYPE html>
<html lang="en">
<head>
<meta charset="utf-8">
<title>Lorenz Vahle – Accident Reports Banner</title>
<link rel="stylesheet" href="https://fonts.googleapis.com/css2?family=Bebas+Neue&family=Roboto:wght@400;500;700&family=Roboto+Condensed:wght@700&display=swap">
<style>
  :root {
    --stage: #808080;
    --ink: #231f20;
    --red: #ed1c24;
    --white: #ffffff;
    --photo-a: #c9d4da;
    --photo-b: #e8c21c;
    --photo-c: #d8321f;
    --photo-d: #3a3a3a;
  }
  * { margin: 0; padding: 0; box-sizing: border-box; }
  html, body {
    width: 1200px; height: 592px; overflow: hidden;
    background: var(--stage);
  }
  .banner {
    position: absolute; left: 63px; top: 117px;
    width: 1074px; height: 358px;
    background: var(--ink);
    overflow: hidden;
  }
  .banner-shapes { position: absolute; inset: 0; }
  .headline {
    position: absolute; left: 540px; width: 400px; top: 8px;
    text-align: center;
    font-family: "Bebas Neue", "Oswald", sans-serif;
    font-weight: 400;
    line-height: 1;
  }
  .headline span { display: block; }
  .headline .line-1 { color: var(--red); font-size: 74px; height: 70px; }
  .headline .line-2 { color: var(--red); font-size: 64px; height: 59px; margin-top: 2px; }
  .headline .line-3 { color: var(--white); font-size: 64px; }
  .brand {
    position: absolute; left: 925px; width: 140px; top: 88px;
    text-align: center; color: var(--white);
    font-family: "Roboto", sans-serif;
  }
  .brand-name { font-size: 13.5px; font-weight: 400; letter-spacing: 1.4px; white-space: nowrap; }
  .brand-sub { font-size: 7.4px; letter-spacing: 1px; line-height: 11px; margin-top: 3px; white-space: nowrap; }
  .service {
    position: absolute; top: 197px; width: 190px;
    text-align: center; color: var(--white);
    font-family: "Roboto", sans-serif;
  }
  .service svg { display: block; margin: 0 auto; }
  .service-label { font-size: 17px; font-weight: 500; margin-top: 6px; white-space: nowrap; }
  .service--reports { left: 455px; }
  .service--evaluation { left: 656px; }
  .service--advice { left: 857px; }
  .contact {
    position: absolute; top: 306px; height: 50px;
    display: flex; align-items: center; gap: 10px;
    color: var(--white);
    white-space: nowrap;
  }
  .contact--phone { left: 499px; font-family: "Roboto Condensed", sans-serif; font-weight: 700; font-size: 30px; letter-spacing: 0.5px; }
  .contact--web { left: 777px; font-family: "Roboto", sans-serif; font-weight: 500; font-size: 24px; }
</style>
</head>
<body>
<div class="banner">
  <svg class="banner-shapes" width="1074" height="358" viewBox="0 0 1074 358">
    <defs>
      <linearGradient id="photo-tones" x1="0" y1="0" x2="1" y2="1">
        <stop offset="0" stop-color="var(--photo-a)"/>
        <stop offset="0.45" stop-color="var(--photo-b)"/>
        <stop offset="0.7" stop-color="var(--photo-c)"/>
        <stop offset="1" stop-color="var(--photo-d)"/>
      </linearGradient>
    </defs>
    <polygon role="img" aria-label="Photo of a red car crashing into a yellow car during a crash test"
             points="0,0 487,0 372,358 0,358" fill="url(#photo-tones)"/>
    <polygon class="accent-stripe" points="489,0 503,0 444,222 430,222" fill="var(--red)"/>
    <rect class="divider-line" x="396" y="297.5" width="678" height="1.6" fill="var(--white)"/>
    <polygon class="contact-band" points="397,302 1074,302 1074,358 380,358" fill="var(--red)"/>
    <polygon class="contact-edge" points="393,298 396.5,298 378.5,358 375,358" fill="var(--white)"/>
    <polygon class="contact-edge-red" points="388,302 391,302 374,358 371,358" fill="var(--red)"/>
  </svg>

  <h1 class="headline">
    <span class="line-1">Accident</span>
    <span class="line-2">Reports from</span>
    <span class="line-3">The Professional</span>
  </h1>

  <div class="brand">
    <div class="brand-name">LORENZ VAHLE</div>
    <div class="brand-sub">KFZ-SACHVERSTÄNDIGER<br>INGENIEURBÜRO</div>
  </div>

  <div class="service service--reports">
    <svg width="54" height="54" viewBox="0 0 54 54">
      <circle cx="27" cy="27" r="25.5" fill="none" stroke="var(--white)" stroke-width="1.2" stroke-dasharray="1 2"/>
      <circle cx="27" cy="27" r="22" fill="var(--red)"/>
      <path d="M19 14h12l5 5v21H19z" fill="var(--white)"/>
      <g stroke="var(--red)" stroke-width="1.4">
        <line x1="22" y1="22" x2="33" y2="22"/><line x1="22" y1="26" x2="33" y2="26"/>
        <line x1="22" y1="30" x2="33" y2="30"/><line x1="22" y1="34" x2="33" y2="34"/>
      </g>
    </svg>
    <div class="service-label">ACCIDENT REPORTS</div>
  </div>

  <div class="service service--evaluation">
    <svg width="54" height="54" viewBox="0 0 54 54">
      <circle cx="27" cy="27" r="25.5" fill="none" stroke="var(--white)" stroke-width="1.2" stroke-dasharray="1 2"/>
      <circle cx="27" cy="27" r="22" fill="var(--red)"/>
      <rect x="25" y="15" width="13" height="22" rx="1" fill="var(--white)"/>
      <path d="M27 21l2 2 3-3M27 27l2 2 3-3M27 33l2 2 3-3" stroke="var(--red)" stroke-width="1.4" fill="none"/>
      <path d="M14 32l2-6h8v10h-10z" fill="var(--white)"/>
      <circle cx="17" cy="37" r="2" fill="var(--white)"/>
    </svg>
    <div class="service-label">VEHICLE EVALUATION</div>
  </div>

  <div class="service service--advice">
    <svg width="54" height="54" viewBox="0 0 54 54">
      <circle cx="27" cy="27" r="25.5" fill="none" stroke="var(--white)" stroke-width="1.2" stroke-dasharray="1 2"/>
      <circle cx="27" cy="27" r="22" fill="var(--red)"/>
      <circle cx="30" cy="21" r="6" fill="none" stroke="var(--white)" stroke-width="3" stroke-dasharray="2.4 1.4"/>
      <path d="M27.5 21l2 2 3-3" stroke="var(--white)" stroke-width="1.4" fill="none"/>
      <rect x="14" y="30" width="4" height="9" fill="var(--white)"/>
      <path d="M19 31h7l3 2h7l2 2-8 4h-11z" fill="var(--white)"/>
    </svg>
    <div class="service-label">TECHNICAL ADVICE</div>
  </div>

  <div class="contact contact--phone">
    <svg width="24" height="24" viewBox="0 0 24 24" aria-hidden="true">
      <path d="M6 3l3 4-2 2c1 3 4 6 7 7l2-2 4 3-2 3c-7 0-15-8-15-15z" fill="none" stroke="var(--white)" stroke-width="2"/>
    </svg>
    <span>012 555 0148</span>
  </div>

  <div class="contact contact--web">
    <svg width="24" height="24" viewBox="0 0 24 24" aria-hidden="true">
      <g fill="none" stroke="var(--white)" stroke-width="1.8">
        <circle cx="12" cy="12" r="10"/><ellipse cx="12" cy="12" rx="4.5" ry="10"/>
        <line x1="2" y1="12" x2="22" y2="12"/><line x1="4" y1="7" x2="20" y2="7"/><line x1="4" y1="17" x2="20" y2="17"/>
      </g>
    </svg>
    <span>www.vahle-kfz.de</span>
  </div>
</div>
</body>
</html>
```